Torvane Aviation Limited

Started a consulting business 12 months ago and have since moved location and have grown and seek to identify my self to the industry.
Specializing in quality solutions, business documentation and maintenance solution's

Industry/Entity Type

Business

```html
<!DOCTYPE html>
<html lang="en">
<head>
<meta charset="utf-8">
<title>Torvane Aviation Limited – Business Card</title>
<link rel="stylesheet" href="https://fonts.googleapis.com/css2?family=Arimo:wght@400;700&display=swap">
<style>
  :root {
    --page-bg: #e9e7e4;
    --card-light: #ececec;
    --card-mid: #d4d4d4;
    --card-edge: #c6c6c6;
    --accent-blue: #1fa8d4;
    --block-white: #ffffff;
    --ink-dark: #151515;
    --ink-grey: #6d6d6d;
    --label-white: #fbfbfb;
  }
  html, body {
    margin: 0;
    padding: 0;
    width: 1200px;
    height: 675px;
    overflow: hidden;
    background: var(--page-bg);
    font-family: "Arimo", Arial, sans-serif;
  }
  .business-card {
    position: absolute;
    left: 150px;
    top: 80px;
    width: 900px;
    height: 514px;
    overflow: hidden;
    background: radial-gradient(ellipse at 52% 30%, var(--card-light) 0%, var(--card-mid) 55%, var(--card-edge) 100%);
    box-shadow: 0 10px 30px rgba(0,0,0,0.18);
  }
  .accent-band-top {
    position: absolute;
    left: 380px;
    top: 0;
    width: 400px;
    height: 24px;
    background: var(--accent-blue);
  }
  .accent-block-top {
    position: absolute;
    right: 0;
    top: 0;
    width: 120px;
    height: 54px;
    background: var(--block-white);
  }
  .accent-band-bottom {
    position: absolute;
    left: 0;
    top: 375px;
    width: 46px;
    height: 112px;
    background: var(--accent-blue);
  }
  .accent-block-bottom {
    position: absolute;
    left: 46px;
    top: 402px;
    width: 52px;
    height: 112px;
    background: var(--block-white);
  }
  .surname-watermark {
    position: absolute;
    left: 170px;
    top: 70px;
    font-weight: 700;
    font-size: 250px;
    letter-spacing: -8px;
    line-height: 1;
    color: var(--block-white);
    opacity: 0.38;
    white-space: nowrap;
  }
  .identity {
    position: absolute;
    left: 100px;
    top: 190px;
  }
  .person-name {
    margin: 0;
    font-size: 50px;
    line-height: 1;
    letter-spacing: -2px;
    color: var(--ink-dark);
    font-weight: 400;
  }
  .person-name .surname { font-weight: 700; }
  .company-name {
    margin: 2px 0 0 38px;
    font-size: 21px;
    color: var(--ink-grey);
  }
  .contact-list {
    position: absolute;
    left: 555px;
    top: 332px;
    margin: 0;
    font-size: 15px;
    line-height: 21px;
    display: grid;
    grid-template-columns: auto auto;
    column-gap: 6px;
  }
  .contact-list dt {
    color: var(--label-white);
    text-align: right;
  }
  .contact-list dt::after {
    content: " \2022";
  }
  .contact-list dd {
    margin: 0;
    color: var(--ink-grey);
  }
  .contact-list .address-line { display: block; }
</style>
</head>
<body>
  <article class="business-card">
    <div class="accent-band-top"></div>
    <div class="accent-block-top"></div>
    <div class="accent-band-bottom"></div>
    <div class="accent-block-bottom"></div>

    <div class="surname-watermark" aria-hidden="true">hale</div>

    <header class="identity">
      <h1 class="person-name">owen<span class="surname">hale</span></h1>
      <p class="company-name">Torvane Aviation Limited</p>
    </header>

    <dl class="contact-list">
      <dt>email</dt>
      <dd>ohale@torvane.co.nz</dd>
      <dt>phone</dt>
      <dd>+64 21 555 0147</dd>
      <dt>address</dt>
      <dd>
        <span class="address-line">Unit B4, 18 Kestrel Lane</span>
        <span class="address-line">Riverhead 0820</span>
        <span class="address-line">Auckland NZ</span>
      </dd>
    </dl>
  </article>
</body>
</html>
```